Wochen Speiseplan
Zielgruppe
Hospiz
Aufgabenstellung
Wir brauchen für unser Hospiz einen Wochenspeiseplan. Es soll eine Powerpointseite im A4 Format erstellt werden. Wir brauchen 4 unterschiedliche Seiten - für jede Jahreszeit einen Entwurf. Der Speiseplan soll von uns selbst ausgefüllt werden können.
Inhalte: Montag - Sonntag jeweils Mittag- und Abendessen. (Aufgebaut wie ein Stundenplan.). Möglichst große Schriftgröße. In der Fußnote bitte: "Änderungen vorbehalten schreiben". Das ganze soll professionell, aber dennoch liebevoll gestaltet sein. Es soll unseren Bewohnern "Liust machen" draufzuschauen. Der Plan wird jede Woche neu ausgefüllt, ausgedruckt und laminiert. Sollte also einfach zu handhaben sein.
Das Hospiz lebt von Spenden, daher bitte nicht zu aufwendig, dafür aber bezahlbar machen.

```html
<!DOCTYPE html>
<html lang="de">
<head>
<meta charset="utf-8">
<title>Wochen Speiseplan</title>
<link href="https://fonts.googleapis.com/css2?family=Arimo:wght@400;700&display=swap" rel="stylesheet">
<style>
  :root {
    --page-bg: #ffffff;
    --header-red: #c40000;
    --header-text: #ffffff;
    --grid-line: rgba(255,255,255,0.85);
    --panel: rgba(255,255,255,0.72);
    --text: #111111;
    --frost: #cfeaf7;
    --frost-edge: #9fd3ee;
    --photo-warm: #d9c6a8;
    --photo-dark: #5a3d30;
    --photo-green: #b7c98a;
    --photo-cream: #efe6d2;
  }
  html, body {
    margin: 0;
    padding: 0;
    width: 1200px;
    height: 903px;
    overflow: hidden;
    background: var(--page-bg);
    font-family: "Arimo", Arial, sans-serif;
  }
  .sheet {
    position: relative;
    width: 1200px;
    height: 903px;
    overflow: hidden;
  }
  .food-photo {
    position: absolute;
  }
  .food-photo--burger {
    left: 0; top: 0; width: 550px; height: 433px;
    background: linear-gradient(135deg, #e9dcc6 0%, var(--photo-warm) 45%, #9fb47a 100%);
  }
  .food-photo--steak {
    left: 558px; top: 0; width: 642px; height: 416px;
    background: linear-gradient(200deg, #f4efe8 0%, #e6d7c6 40%, var(--photo-dark) 75%, #e9e2d8 100%);
  }
  .food-photo--pesto {
    left: 0; top: 433px; width: 550px; height: 470px;
    background: radial-gradient(ellipse at 45% 70%, var(--photo-green) 0%, #dfe3d6 55%, #f2f2ef 100%);
  }
  .food-photo--penne {
    left: 558px; top: 416px; width: 642px; height: 487px;
    background: linear-gradient(160deg, #f3eee4 0%, var(--photo-cream) 45%, #e2c98e 80%, #8fae63 100%);
  }
  .frost-frame {
    position: absolute;
    left: 0; top: 0;
    width: 1200px; height: 903px;
  }
  .menu-table {
    position: absolute;
    left: 75px;
    top: 91px;
    width: 1067px;
    height: 679px;
    border-collapse: collapse;
    table-layout: fixed;
    background: var(--panel);
    box-shadow: 0 2px 8px rgba(0,0,0,0.25);
  }
  .menu-table th, .menu-table td {
    border: 1px solid var(--grid-line);
    text-align: center;
    color: var(--text);
  }
  .menu-table .day {
    height: 60px;
    background: var(--header-red);
    color: var(--header-text);
    font-weight: 400;
    font-size: 17px;
  }
  .meal-label {
    display: block;
    font-weight: 700;
    font-size: 18px;
    letter-spacing: 0.5px;
  }
  .menu-table .meal {
    font-size: 19.5px;
    line-height: 24px;
    vertical-align: middle;
    padding: 0 4px;
  }
  .row-label td {
    height: 0;
    border-bottom: none;
    border-top: none;
  }
  .section-title {
    position: absolute;
    left: 75px;
    width: 1067px;
    text-align: center;
    font-weight: 700;
    font-size: 18px;
    color: var(--text);
    letter-spacing: 0.5px;
  }
  .section-title--lunch { top: 168px; }
  .section-title--dinner { top: 433px; }
  .footnote {
    position: absolute;
    left: 911px;
    top: 846px;
    font-size: 17px;
    color: var(--text);
  }
</style>
</head>
<body>
<main class="sheet">
  <div class="food-photo food-photo--burger" role="img" aria-label="Foto eines Burgers mit Salat"></div>
  <div class="food-photo food-photo--steak" role="img" aria-label="Foto eines Schokoladenkuchens auf einem Teller"></div>
  <div class="food-photo food-photo--pesto" role="img" aria-label="Foto von Nudeln mit grünem Pesto auf einem weißen Teller"></div>
  <div class="food-photo food-photo--penne" role="img" aria-label="Foto von Penne mit Rahmsoße und Kräutern"></div>

  <svg class="frost-frame" viewBox="0 0 1200 903" role="img" aria-label="Winterlicher Eisrahmen um den Speiseplan">
    <path d="M60 48 Q300 28 600 44 T1160 58 L1160 96 Q800 80 600 90 T60 92 Z" fill="var(--frost)" opacity="0.85"/>
    <path d="M28 58 L80 50 L86 500 L62 520 L40 480 Z" fill="var(--frost)" opacity="0.85"/>
    <path d="M1112 628 L1170 620 L1174 790 L890 795 L880 760 L1118 752 Z" fill="var(--frost)" opacity="0.85"/>
  </svg>

  <table class="menu-table">
    <thead>
      <tr>
        <th class="day">MONTAG</th>
        <th class="day">DIENSTAG</th>
        <th class="day">MITTWOCH</th>
        <th class="day">DONNERSTAG</th>
        <th class="day">FREITAG</th>
        <th class="day">SAMSTAG</th>
        <th class="day">SONNTAG</th>
      </tr>
    </thead>
    <tbody>
      <tr style="height:265px">
        <td class="meal">Pizza Salami mit Salat und Pudding</td>
        <td class="meal">Pizza Salami mit Salat und Pudding</td>
        <td class="meal">Pizza Salami mit Salat und Pudding</td>
        <td class="meal">Pizza Salami mit Salat und Pudding</td>
        <td class="meal">Pizza Salami mit Salat und Pudding</td>
        <td class="meal">Pizza Salami mit Salat und Pudding</td>
        <td class="meal">Pizza Salami mit Salat und Pudding</td>
      </tr>
      <tr style="height:354px">
        <td class="meal">Gebratene Nudeln mit frischem Gemüse</td>
        <td class="meal">Gebratene Nudeln mit frischem Gemüse</td>
        <td class="meal">Gebratene Nudeln mit frischem Gemüse</td>
        <td class="meal">Gebratene Nudeln mit frischem Gemüse</td>
        <td class="meal">Gebratene Nudeln mit frischem Gemüse</td>
        <td class="meal">Gebratene Nudeln mit frischem Gemüse</td>
        <td class="meal">Gebratene Nudeln mit frischem Gemüse</td>
      </tr>
    </tbody>
  </table>

  <div class="section-title section-title--lunch">MITTAGS:</div>
  <div class="section-title section-title--dinner">ABENDS:</div>

  <p class="footnote" style="margin:0">Änderungen vorbehalten</p>
</main>
</body>
</html>
```